Brightloom Orthodontics business card design

Need a business card design that reflects our re-branding (orthodontic office - braces) and a new partnership with a pediatric dental office. We would like to include "for adults and children" on the card as well so adults know they are welcome to get their braces here as well. Office design is modern and would like business card to reflect a modern type look. Here's the text we would like to be included on the card:

Daniel Pruvost, DDS, MSD
5214 West Halden Avenue, Suite 204
Mansfield, TX 76099
682-555-4817
www.brightloomortho.example
info@brightloomortho.example
Updates

Can we add the following to the existing designs? Daniel Pruvost, DDS, MSD 5214 West Halden Avenue, Suite 204 Mansfield, TX 76099 682-555-4817

Does anyone have any more vertical designs available? Thanks!

Industry/Entity Type

Dental

```html
<!DOCTYPE html>
<html lang="en">
<head>
<meta charset="utf-8">
<title>Brightloom Orthodontics – Business Card</title>
<link rel="stylesheet" href="https://fonts.googleapis.com/css2?family=Titillium+Web:wght@400;600;700;900&display=swap">
<style>
  :root {
    --backdrop: #e9e7e4;
    --card: #ffffff;
    --card-edge: #111111;
    --ink: #1b1b1b;
    --blue: #1b7cc4;
    --pink: #ec0e8c;
    --green: #8cc63f;
    --orange: #f7941d;
    --white: #ffffff;
  }
  * { box-sizing: border-box; margin: 0; padding: 0; }
  html, body { width: 1200px; height: 960px; overflow: hidden; }
  body {
    background: var(--backdrop);
    font-family: "Titillium Web", Arial, sans-serif;
    display: flex;
    align-items: center;
    justify-content: center;
  }
  .card {
    position: relative;
    width: 520px;
    height: 800px;
    background: var(--card);
    border: 10px solid var(--card-edge);
    border-radius: 6px;
  }
  .brand {
    position: absolute;
    top: 70px;
    right: 36px;
    text-align: right;
  }
  .brand-name {
    display: flex;
    align-items: center;
    justify-content: flex-end;
    gap: 14px;
    font-size: 46px;
    font-weight: 900;
    line-height: 1;
    color: var(--ink);
    letter-spacing: 0.5px;
  }
  .brand-mark {
    width: 34px;
    height: 34px;
    border-radius: 50%;
    background: var(--blue);
    flex: none;
  }
  .brand-word-2 {
    display: block;
    font-size: 50px;
    font-weight: 900;
    color: var(--ink);
    line-height: 1.05;
  }
  .tagline {
    margin-top: 6px;
    font-size: 24px;
    font-weight: 700;
    color: var(--green);
    line-height: 1;
  }
  .doctor {
    position: absolute;
    top: 288px;
    right: 36px;
    text-align: right;
    color: var(--ink);
  }
  .doctor-name {
    font-size: 36px;
    font-weight: 600;
    line-height: 1;
    letter-spacing: 1px;
  }
  .doctor-credentials {
    font-size: 20px;
    font-weight: 400;
    letter-spacing: 1px;
    margin-top: 4px;
  }
  .contacts {
    position: absolute;
    left: 26px;
    right: 54px;
    top: 388px;
    list-style: none;
  }
  .contact {
    display: flex;
    align-items: center;
    gap: 22px;
    padding: 0 22px;
    color: var(--white);
    font-size: 24px;
    font-weight: 400;
    line-height: 1.15;
    letter-spacing: 0.5px;
  }
  .contact svg { width: 24px; height: 24px; flex: none; fill: var(--white); }
  .contact--address { background: var(--blue); height: 124px; }
  .contact--phone   { background: var(--pink); height: 84px; }
  .contact--email   { background: var(--green); height: 84px; font-size: 22px; }
  .contact--web     { background: var(--orange); height: 104px; font-size: 22px; }
</style>
</head>
<body>
  <article class="card">
    <header class="brand">
      <div class="brand-name"><span class="brand-mark"></span>Brightloom</div>
      <span class="brand-word-2">Orthodontics</span>
      <p class="tagline">For Adults and Children</p>
    </header>

    <section class="doctor">
      <h1 class="doctor-name">Daniel Pruvost</h1>
      <p class="doctor-credentials">DDS, MSD</p>
    </section>

    <ul class="contacts">
      <li class="contact contact--address">
        <svg viewBox="0 0 24 24" aria-hidden="true"><path d="M12 1a8 8 0 0 0-8 8c0 6 8 14 8 14s8-8 8-14a8 8 0 0 0-8-8zm0 11a3 3 0 1 1 0-6 3 3 0 0 1 0 6z"/></svg>
        <span>5214 West Halden Avenue,<br>Suite 204 Mansfield,<br>TX 76099</span>
      </li>
      <li class="contact contact--phone">
        <svg viewBox="0 0 24 24" aria-hidden="true"><path d="M7 1h10a2 2 0 0 1 2 2v18a2 2 0 0 1-2 2H7a2 2 0 0 1-2-2V3a2 2 0 0 1 2-2zm0 3v14h10V4H7zm5 15.5a1 1 0 1 0 0 2 1 1 0 0 0 0-2z"/></svg>
        <span>682-555-4817</span>
      </li>
      <li class="contact contact--email">
        <svg viewBox="0 0 24 24" aria-hidden="true"><path d="M2 5h20v14H2V5zm2 2v.5l8 5.5 8-5.5V7H4zm0 3v7h16v-7l-8 5.5L4 10z"/></svg>
        <span>info@brightloomortho.example</span>
      </li>
      <li class="contact contact--web">
        <svg viewBox="0 0 24 24" aria-hidden="true"><path d="M12 2a10 10 0 1 0 0 20 10 10 0 0 0 0-20zm7.9 9h-3.4a15 15 0 0 0-1.6-6.4A8 8 0 0 1 19.9 11zM12 4c1.2 1.5 2.3 4 2.5 7h-5C9.7 8 10.8 5.5 12 4zM9.1 4.6A15 15 0 0 0 7.5 11H4.1a8 8 0 0 1 5-6.4zM4.1 13h3.4a15 15 0 0 0 1.6 6.4A8 8 0 0 1 4.1 13zm5.4 0h5c-.2 3-1.3 5.5-2.5 7-1.2-1.5-2.3-4-2.5-7zm5.4 6.4a15 15 0 0 0 1.6-6.4h3.4a8 8 0 0 1-5 6.4z"/></svg>
        <span>www.brightloomortho.example</span>
      </li>
    </ul>
  </article>
</body>
</html>
```